CPA Graduation Party

I need to make simple invitation for my sister's recent success, passing the CPA (Certified Public Accountant) exam. It is a surprise party. I want very simple and professional looking invitation. My only requirements are that you don't use any graduation caps or gowns due to the fact that it's not an actual graduation. It's a series of exams that she passes. Be creative with the design but once again, keep it professional. I have attached a font called iScriptSTD. I liked the font so was thinking about using it. But it's not necessary. If you have something slimier or better, please use it.

I was planning on printing on a specific kind of paper. It's called pearlized ivory cardstock. It has a little coating and shine on it and since it's ivory, I was thinking about the main color of the invitation to be burgundy type. For example, see the following RGB: R204, G0, B102.

Party info:
Name: Ravina
Date & Time: Saturday, March 8th, 2014 at 6:00pm
Location: Seher Mahal. 418 Brambleford Lane Parsippany, NJ 07291

I know I didn't provide a lot of info for the invite but please be creative.  Use general knowledge and other formal party invites as examples. I am not looking for a name, date and location as three bullets on the card.

Also, I forgot to mention the size of the invite.  It should be 5.5x8.5.  Thank you.

• graduation caps and/or gowns

```html
<!DOCTYPE html>
<html lang="en">
<head>
<meta charset="utf-8">
<title>Ravina – CPA Celebration Invitation</title>
<link rel="stylesheet" href="https://fonts.googleapis.com/css2?family=Goudy+Bookletter+1911&family=Kaushan+Script&family=Lobster+Two:ital,wght@1,700&display=swap">
<style>
  :root {
    --berry: #c8146a;
    --berry-deep: #b50f5e;
    --ivory: #ffffff;
    --soft: rgba(255, 255, 255, 0.85);
  }
  * { margin: 0; padding: 0; box-sizing: border-box; }
  html, body { width: 778px; height: 1200px; overflow: hidden; background: var(--berry); }
  .invite {
    position: relative;
    width: 778px;
    height: 1200px;
    background: var(--berry);
    color: var(--ivory);
    text-align: center;
    overflow: hidden;
  }
  .seal {
    position: absolute;
    left: 50%;
    top: 10px;
    width: 170px;
    height: 170px;
    margin-left: -85px;
    border-radius: 50%;
    background: var(--ivory);
    border: 6px solid var(--berry-deep);
    box-shadow: 0 0 0 3px var(--ivory);
  }
  .class-line {
    position: absolute;
    top: 205px;
    left: 0;
    width: 100%;
    font-family: "Lobster Two", cursive;
    font-style: italic;
    font-weight: 700;
    font-size: 46px;
    letter-spacing: 1px;
  }
  .rule-thick, .rule-thin {
    position: absolute;
    left: 0;
    width: 100%;
    background: var(--ivory);
  }
  .rule-thick { top: 290px; height: 10px; }
  .rule-thin { top: 312px; height: 3px; }
  .lead {
    position: absolute;
    top: 378px;
    left: 0;
    width: 100%;
    font-family: "Goudy Bookletter 1911", serif;
    font-size: 42px;
    line-height: 1.3;
  }
  .honoree {
    position: absolute;
    top: 560px;
    left: 0;
    width: 100%;
    font-family: "Kaushan Script", cursive;
    font-size: 112px;
    letter-spacing: 4px;
    line-height: 1;
  }
  .flourish {
    position: absolute;
    top: 688px;
    left: 50%;
    width: 110px;
    height: 26px;
    margin-left: -55px;
    border-radius: 13px;
    background: var(--soft);
  }
  .when {
    position: absolute;
    top: 790px;
    left: 0;
    width: 100%;
    font-family: "Goudy Bookletter 1911", serif;
    font-size: 46px;
    line-height: 1.25;
  }
  .where {
    position: absolute;
    top: 955px;
    left: 0;
    width: 100%;
    font-family: "Goudy Bookletter 1911", serif;
    font-size: 46px;
    line-height: 1.25;
  }
  .wave {
    position: absolute;
    left: 0;
    bottom: 0;
    width: 778px;
    height: 110px;
  }
</style>
</head>
<body>
  <main class="invite">
    <div class="seal" role="img" aria-label="Certification seal"></div>
    <p class="class-line">Class of 2014 Graduate</p>
    <div class="rule-thick"></div>
    <div class="rule-thin"></div>

    <p class="lead">Join us for a graduation party<br>honoring</p>
    <h1 class="honoree">RAVINA</h1>
    <div class="flourish" role="img" aria-label="Decorative flourish"></div>

    <p class="when">Saturday, March 8th, 2014<br>at 6:00pm</p>
    <p class="where">Seher Mahal. 418 Brambleford Lane<br>Parsippany, NJ 07291</p>

    <svg class="wave" viewBox="0 0 778 110" aria-hidden="true">
      <path d="M0 62 C 220 108, 520 10, 778 30" fill="none" stroke="#ffffff" stroke-width="3"/>
      <path d="M0 80 C 220 126, 520 28, 778 48 L 778 110 L 0 110 Z" fill="#ffffff"/>
    </svg>
  </main>
</body>
</html>
```